Landing page for B2B Product Idea Validation Event

We need a single landing page design for the world’s first competition to help aspiring entrepreneurs to validate their new business 2 business (B2B) web application ideas.

We like the following landing pages as examples for the structure and sectioning we would like to see for this landing page:
http://ny.brivolex.com/
https://tarvel.com/tarvelfest

There should be around 5 sections including an application form.

Target Market(s)

Entrepreneurs

Industry/Entity Type

Business Software

Number of Pages Required

1 page

Font styles to use
Serif

Requirements
Must have
• Colors must be similar to the logo provided.

```html
<!DOCTYPE html>
<html lang="en">
<head>
<meta charset="utf-8">
<title>Kestrova – B2B Idea Validation Event</title>
<link rel="stylesheet" href="https://fonts.googleapis.com/css2?family=Arimo:wght@400;700&family=Libre+Baskerville:ital,wght@0,400;0,700;1,400&display=swap">
<style>
  :root {
    --page-bg: #e6e6e6;
    --sheet: #ffffff;
    --brand-blue: #1c5aa6;
    --nav-blue: #1f5fae;
    --band-blue: #3d99e3;
    --attrib-blue: #1a5aa3;
    --heading-grey: #555555;
    --body-grey: #8a8a8a;
    --footer-dark: #2d2d2f;
    --button-grey: #666666;
    --white: #ffffff;
    --serif: "Libre Baskerville", Georgia, serif;
    --sans: "Arimo", Arial, sans-serif;
  }
  * { box-sizing: border-box; margin: 0; padding: 0; }
  html, body { width: 864px; height: 1200px; overflow: hidden; }
  body { background: var(--page-bg); position: relative; font-family: var(--sans); }
  .sheet { position: absolute; left: 30px; top: 0; width: 805px; height: 1200px; background: var(--sheet); }
  .abs { position: absolute; }

  /* header */
  .brand { left: 84px; top: 2px; display: flex; align-items: center; gap: 6px; color: var(--brand-blue); font: 700 21px/24px var(--sans); letter-spacing: 0.5px; }
  .brand-dot { width: 12px; height: 12px; border-radius: 50%; background: var(--brand-blue); }
  .nav { top: 33px; left: 0; width: 864px; font: 400 9.5px/12px var(--sans); }
  .nav a { position: absolute; color: var(--nav-blue); text-decoration: none; white-space: nowrap; }
  .nav a.current { text-decoration: underline; }

  /* hero */
  .hero { left: 30px; top: 48px; width: 805px; height: 322px; background: radial-gradient(ellipse at 62% 35%, #6e9ad8 0%, #3f71c4 40%, #2a56a8 75%, #22479a 100%); box-shadow: 0 2px 3px rgba(0,0,0,0.35); }
  .hero-title { left: 30px; top: 168px; width: 805px; text-align: center; color: var(--white); font: 400 32px/40px var(--serif); }
  .hero-tagline { left: 30px; top: 218px; width: 805px; text-align: center; color: var(--white); font: italic 400 17px/22px var(--serif); }

  /* intro */
  .section-title { color: var(--heading-grey); font: 700 22px/26px var(--sans); text-transform: uppercase; }
  .section-text { left: 126px; width: 620px; color: var(--body-grey); font: 400 10.4px/10.5px var(--sans); letter-spacing: 0.9px; }

  /* testimonial */
  .band { left: 30px; top: 596px; width: 805px; height: 208px; background: var(--band-blue); }
  .quote-mark { color: var(--white); font: 700 48px/40px var(--serif); }
  .quote-text { left: 174px; top: 646px; width: 530px; color: var(--white); font: 700 10.5px/12.4px var(--sans); letter-spacing: 1.6px; text-transform: uppercase; }
  .attribution { left: 30px; top: 758px; width: 805px; text-align: center; color: var(--attrib-blue); font: 700 8.5px/13px var(--sans); letter-spacing: 1.3px; text-transform: uppercase; }

  /* team */
  .team-title { left: 30px; top: 812px; width: 805px; text-align: center; color: #333; font: 400 17px/22px var(--serif); letter-spacing: 2px; }
  .rule { height: 1px; background: #333; top: 823px; width: 64px; }
  .member { width: 200px; text-align: center; top: 842px; }
  .member-photo { width: 110px; height: 88px; border-radius: 50%; margin: 0 auto; }
  .member-name { margin-top: 10px; color: #222; font: 400 13.5px/18px var(--serif); letter-spacing: 0.8px; }
  .member-bio { margin-top: 4px; color: #555; font: italic 400 9.2px/10px var(--serif); letter-spacing: 0.6px; }

  /* contact */
  .contact { left: 30px; top: 1017px; width: 805px; height: 183px; background: var(--footer-dark); }
  .contact-title { left: 30px; top: 1026px; width: 805px; text-align: center; color: var(--white); font: 400 16px/22px var(--serif); letter-spacing: 1.5px; }
  .contact-title span { border-bottom: 1px solid var(--white); padding-bottom: 1px; }
  .field { background: var(--white); border: 2px solid #cfcfcf; color: #999; font: 400 11.5px/18px var(--serif); letter-spacing: 1.5px; padding: 1px 6px; }
  .send { left: 485px; top: 1152px; width: 94px; height: 18px; background: var(--button-grey); color: var(--white); text-align: center; font: 400 13px/18px var(--serif); letter-spacing: 1px; }
  .copyright { left: 30px; top: 1189px; width: 805px; text-align: center; color: #999; font: 400 8px/10px var(--serif); letter-spacing: 0.5px; }
</style>
</head>
<body>
  <div class="sheet"></div>

  <header>
    <div class="abs brand"><span class="brand-dot"></span>Kestrova</div>
    <nav class="abs nav">
      <a class="current" style="left:153px">HOME</a>
      <a style="left:211px">ABOUT US</a>
      <a style="left:289px">EXHIBITION</a>
      <a style="left:372px">EXHIBIT/SPOSNOR</a>
      <a style="left:493px">APPLICATION FORM</a>
    </nav>
  </header>

  <section>
    <div class="abs hero" role="img" aria-label="Blue-tinted photo of a laptop keyboard with a notebook and pen on a desk"></div>
    <svg class="abs" style="left:92px;top:198px" width="22" height="26" viewBox="0 0 22 26"><path d="M16 3 L5 13 L16 23" fill="none" stroke="#fff" stroke-width="4" stroke-linecap="round" stroke-linejoin="round"/></svg>
    <svg class="abs" style="left:754px;top:198px" width="22" height="26" viewBox="0 0 22 26"><path d="M6 3 L17 13 L6 23" fill="none" stroke="#fff" stroke-width="4" stroke-linecap="round" stroke-linejoin="round"/></svg>
    <h1 class="abs hero-title">Your example text goes here!</h1>
    <p class="abs hero-tagline">Tagline goes here! (Optional)</p>
  </section>

  <section>
    <h2 class="abs section-title" style="left:171px;top:382px">Kestrova brings together the new<br>world of marketing technology</h2>
    <p class="abs section-text" style="top:441px">From Top 100 to emerging start-ups, intnovators across industries converge to discuss the new era of advertising and marketing technology. This 20th Anniversary of ad:nexa looks to be the most comprehensive yet with exciting hands-on exhibitions, invaluable<br>learning opportunities, and the players reimaging the future of the industry.</p>
    <h2 class="abs section-title" style="left:170px;top:488px">Have better conversations with more<br>potential partners</h2>
    <p class="abs section-text" style="top:546px">It's a new world, where technologies across industries are converging and it calls for a change in the way we think about marketing and advertising. We bring together leading edge brands, agencies, and tech providers to create a more dynamic experience than ever before.<br>Join the conversation, share your insights, and get a competitive edge.</p>
  </section>

  <section>
    <div class="abs band"></div>
    <div class="abs quote-mark" style="left:126px;top:646px">&ldquo;</div>
    <div class="abs quote-mark" style="left:706px;top:646px">&rdquo;</div>
    <svg class="abs" style="left:88px;top:692px" width="12" height="16" viewBox="0 0 12 16"><path d="M9 2 L3 8 L9 14" fill="none" stroke="#fff" stroke-width="2"/></svg>
    <svg class="abs" style="left:766px;top:692px" width="12" height="16" viewBox="0 0 12 16"><path d="M3 2 L9 8 L3 14" fill="none" stroke="#fff" stroke-width="2"/></svg>
    <blockquote class="abs quote-text">For 20 years, Kestrova has been the go-to-event for the entire online advertising industry. It's great to see the event reenergize and expand to cover the essential topics of today, including marketing tech, analytics, virtual reality and wearables, among others . I'm especially&nbsp; looking forward to hearing the keynotes, including the perennial&nbsp; thought leader for the industry, Orlen Vastrick</blockquote>
    <p class="abs attribution">Talvin Marosh<br>Quillmont Advisory</p>
  </section>

  <section>
    <div class="abs rule" style="left:282px"></div>
    <div class="abs rule" style="left:516px"></div>
    <h2 class="abs team-title">Meet our team</h2>
    <div class="abs member" style="left:130px">
      <div class="member-photo" role="img" aria-label="Portrait photo of team member Mirela Hartwin" style="background:radial-gradient(circle at 50% 45%, #c9a489 0%, #7a5440 55%, #3b2a22 100%)"></div>
      <p class="member-name">Mirela Hartwin</p>
      <p class="member-bio">This is an example text<br>you can easily<br>edit it<br>hello world!</p>
    </div>
    <div class="abs member" style="left:333px">
      <div class="member-photo" role="img" aria-label="Black and white portrait photo of team member Corin Ashdale" style="background:radial-gradient(circle at 45% 55%, #b8b8b8 0%, #6e6e6e 50%, #222 100%)"></div>
      <p class="member-name">Corin Ashdale</p>
      <p class="member-bio">This is an example text<br>you can easily<br>edit it<br>hello world!</p>
    </div>
    <div class="abs member" style="left:531px">
      <div class="member-photo" role="img" aria-label="Portrait photo of team member Lenna Virosz" style="background:radial-gradient(circle at 50% 50%, #d9b3a0 0%, #9a6a4e 45%, #8f9a78 100%)"></div>
      <p class="member-name">Lenna Virosz</p>
      <p class="member-bio">This is an example text<br>you can easily<br>edit it<br>hello world!</p>
    </div>
  </section>

  <footer>
    <div class="abs contact"></div>
    <h2 class="abs contact-title"><span>Contact us</span></h2>
    <div class="abs field" style="left:182px;top:1067px;width:192px;height:22px">Full name</div>
    <div class="abs field" style="left:182px;top:1097px;width:192px;height:22px">Email id</div>
    <div class="abs field" style="left:182px;top:1127px;width:282px;height:43px">Message</div>
    <div class="abs send">Send</div>
    <p class="abs copyright">Kestrova 2016 (C)</p>
  </footer>
</body>
</html>
```